Creative Web Site to Sell Geology Classes for Homeschooling

I am starting a business to sell a variety of geology classes for homeschoolers. I am targeting classes for kids with dyslexia, although others will benefit as well. The classes will be delivered by mail. Each class will have a video, a manual, and rock samples. I need a landing page that I can link over to seven other pages, a page with a template for products, and a template of the pages that will not have products. All should be easy to edit. All pages should display well with handheld devices (phones), as well as desktops.

```html
<!DOCTYPE html>
<html lang="en">
<head>
<meta charset="utf-8">
<title>Stonefield Academy – Geology Classes</title>
<link href="https://fonts.googleapis.com/css2?family=Open+Sans:wght@400;600;700;800&display=swap" rel="stylesheet">
<style>
:root{
  --coral:#e8705a;
  --red:#ef5a52;
  --yellow:#f5bf36;
  --green:#5ccf9c;
  --purple:#574a6c;
  --ink:#1d1d1f;
  --text:#444;
  --muted:#8a8a8a;
  --mist:#f3f1f2;
  --white:#ffffff;
  --footer:#232224;
}
*{margin:0;padding:0;box-sizing:border-box}
html,body{width:1200px;height:4167px;overflow:hidden}
body{font-family:"Open Sans",Arial,sans-serif;color:var(--text);background:var(--white);position:relative}
.abs{position:absolute}
.btn{position:absolute;display:inline-block;background:var(--green);color:var(--white);font-weight:700;font-size:17px;text-transform:uppercase;border-radius:4px;text-align:center;letter-spacing:.3px}
.section-title{position:absolute;left:0;width:1200px;text-align:center;font-weight:800;font-size:31px;color:var(--ink);letter-spacing:.5px}
.title-rule{position:absolute;left:577px;width:46px;height:3px;background:#c7c4c6}

/* header */
.site-header{position:absolute;top:0;left:0;width:1200px;height:117px;background:var(--white)}
.brand{position:absolute;left:145px;top:30px;display:flex;align-items:center;gap:12px}
.brand-dot{width:50px;height:50px;border-radius:50%;background:var(--coral)}
.brand-name{font-weight:800;font-size:26px;line-height:1.05;color:var(--coral);text-transform:uppercase}
.follow{position:absolute;left:645px;top:22px;display:flex;align-items:center;gap:6px;font-size:12px;font-weight:700;color:#777;letter-spacing:.5px}
.follow span.soc{width:24px;height:24px;border-radius:50%;background:#2b5aa8;display:inline-block}
.phone-box{position:absolute;left:861px;top:4px;width:42px;height:42px;background:#d9d9d9;border-radius:3px}
.call{position:absolute;left:917px;top:12px;font-size:12px;font-weight:700;color:#888;letter-spacing:.5px}
.call strong{display:block;font-size:23px;color:var(--red);font-weight:800;letter-spacing:0;line-height:1.2}
.main-nav{position:absolute;left:533px;top:78px;display:flex;height:39px}
.main-nav a{display:flex;align-items:center;justify-content:center;color:var(--white);font-weight:700;font-size:13px;text-transform:uppercase;text-decoration:none}

/* hero */
.hero{position:absolute;top:117px;left:0;width:1200px;height:555px;background:radial-gradient(ellipse at 62% 45%,#c89a82 0%,#8e4f3c 45%,#5a2a22 100%)}
.hero h1{position:absolute;left:139px;top:139px;font-size:60px;line-height:1.08;font-weight:800;color:var(--white);letter-spacing:1px}
.dots{position:absolute;top:506px;left:543px;display:flex;gap:14px;align-items:center}
.dots i{width:8px;height:8px;border-radius:50%;background:#fff;display:block;opacity:.85}
.dots i.on{width:14px;height:14px;background:transparent;border:2px solid #fff}

/* classes */
.classes{position:absolute;top:672px;left:0;width:1200px;height:661px;background:var(--mist)}
.class-card{position:absolute;top:170px;width:228px;height:400px;color:var(--white);box-shadow:0 6px 14px rgba(0,0,0,.18)}
.class-card .photo{height:208px}
.class-card h3{font-size:14px;font-weight:800;margin:18px 22px 10px}
.class-card p{font-size:12.5px;line-height:1.4;margin:0 22px}
.class-card .more{display:inline-block;margin:16px 22px;background:var(--white);color:#333;font-size:10px;font-weight:800;padding:5px 11px;border-radius:2px}

/* welcome */
.welcome{position:absolute;top:1333px;left:0;width:1200px;height:534px;background:var(--white)}
.welcome h2{position:absolute;left:145px;top:93px;font-size:25px;font-weight:800;color:var(--ink);line-height:1.3}
.welcome h2 span{display:block;font-size:44px;color:var(--yellow);line-height:1.15}
.welcome .rule{position:absolute;left:145px;top:178px;width:46px;height:3px;background:#c7c4c6}
.welcome p{position:absolute;left:145px;top:220px;width:420px;font-size:14.5px;line-height:1.52}
.welcome-photo{position:absolute;left:592px;top:56px;width:464px;height:422px;background:linear-gradient(135deg,#6d8fa8 0%,#a9c2d6 45%,#5a4a44 100%)}

/* news */
.news{position:absolute;top:1867px;left:0;width:1200px;height:647px;background:var(--mist)}
.news-card{position:absolute;top:158px;width:292px;height:408px;background:var(--white);box-shadow:0 2px 8px rgba(0,0,0,.08)}
.news-card .photo{height:197px}
.news-card h3{font-size:15px;font-weight:800;color:var(--ink);margin:24px 24px 8px;line-height:1.3;text-transform:uppercase}
.news-card p{font-size:13.5px;line-height:1.38;margin:0 24px}
.news-card .more{display:inline-block;margin:16px 24px;background:var(--green);color:var(--white);font-size:11px;font-weight:800;padding:6px 12px;border-radius:3px}

/* testimonials */
.testimonials{position:absolute;top:2514px;left:0;width:1200px;height:592px;background:var(--white)}
.quote{position:absolute;left:333px;top:180px;width:534px;text-align:center;font-size:17.5px;line-height:1.5;color:#333}
.qmark{position:absolute;font-size:80px;font-weight:800;color:var(--green);line-height:1}
.person{position:absolute;text-align:center;width:160px}
.person .avatar{margin:0 auto;border-radius:50%;background:linear-gradient(160deg,#9a8a80,#4d4541);border:3px solid #fff;box-shadow:0 2px 6px rgba(0,0,0,.2)}
.person b{display:block;font-size:11.5px;font-weight:800;color:var(--ink);margin-top:8px}
.person small{display:block;font-size:9px;color:var(--muted);text-transform:uppercase}

/* schedule */
.schedule{position:absolute;top:3106px;left:0;width:1200px;height:422px;background:linear-gradient(180deg,#2c3d5a 0%,#6e5a52 40%,#9a5b3e 75%,#6a3a28 100%)}
.schedule h2{position:absolute;top:88px;width:1200px;text-align:center;font-size:36px;font-weight:800;color:var(--white)}
.schedule p{position:absolute;left:370px;top:166px;width:460px;text-align:center;font-size:17px;line-height:1.42;color:var(--white)}

/* features */
.features{position:absolute;top:3528px;left:0;width:1200px;height:258px;display:flex}
.feature{width:400px;height:258px;position:relative;color:var(--white)}
.feature svg{position:absolute;left:60px;top:40px}
.feature h3{position:absolute;left:60px;top:128px;font-size:17px;font-weight:800;text-transform:uppercase}
.feature p{position:absolute;left:60px;top:160px;width:250px;font-size:14px;line-height:1.35;opacity:.92}

/* footer */
.site-footer{position:absolute;top:3786px;left:0;width:1200px;height:381px;background:var(--footer);color:#ddd}
.site-footer .brand{left:145px;top:115px}
.site-footer .brand-dot{width:70px;height:70px}
.site-footer .brand-name{font-size:36px}
.f-col{position:absolute;top:68px;font-size:12px}
.f-col h4{font-size:12px;font-weight:800;color:var(--white);text-transform:uppercase;margin-bottom:18px}
.f-col li{list-style:none;line-height:1.4;margin-bottom:4px;display:flex;gap:12px;align-items:flex-start}
.f-col .ico{width:12px;height:12px;margin-top:2px;flex:none}
.f-col .circ{width:22px;height:22px;border-radius:50%;background:#2b5aa8;flex:none}
.f-col.contact li{margin-bottom:20px}
.f-col.connect li{margin-bottom:16px;align-items:center}
.copyright{position:absolute;top:338px;width:1200px;text-align:center;font-size:11.5px;color:#bbb}
</style>
</head>
<body>

<header class="site-header">
  <div class="brand"><span class="brand-dot"></span><span class="brand-name">Stonefield<br>Academy</span></div>
  <div class="follow">FOLLOW US <span class="soc"></span><span class="soc" style="background:#2aa3e0"></span><span class="soc" style="background:#1f5f92"></span></div>
  <div class="phone-box">
    <svg width="42" height="42" viewBox="0 0 42 42"><path d="M15 12c2 0 3 4 3 5s-2 2-2 3c1 3 3 5 6 6 1 0 2-2 3-2s5 1 5 3-2 4-4 4c-7-1-13-7-14-14 0-2 1-5 3-5z" fill="#fff"/></svg>
  </div>
  <div class="call">CALL US NOW<strong>800.555.0142</strong></div>
  <nav class="main-nav">
    <a href="#" style="width:89px;background:var(--coral)">Home</a>
    <a href="#" style="width:103px;background:var(--yellow);margin-left:14px">About Us</a>
    <a href="#" style="width:94px;background:var(--red);margin-left:6px">Classes</a>
    <a href="#" style="width:103px;background:var(--green);margin-left:6px">Programs</a>
    <a href="#" style="width:105px;background:var(--purple)">Contact</a>
  </nav>
</header>

<section class="hero" role="img" aria-label="Hands holding a fossil specimen over reddish rock">
  <h1>GEOLOGY<br>CLASSES</h1>
  <span class="btn" style="left:145px;top:291px;width:147px;height:45px;line-height:45px">Read More</span>
  <div class="dots"><i></i><i></i><i class="on"></i><i></i><i></i></div>
</section>

<section class="classes">
  <h2 class="section-title" style="top:57px">GEOLOGY CLASSES</h2>
  <div class="title-rule" style="top:113px"></div>

  <article class="class-card" style="left:114px;background:var(--coral);transform:rotate(-2deg)">
    <div class="photo" role="img" aria-label="Child examining a rock with a magnifying glass" style="background:linear-gradient(135deg,#7aa860,#c9b48c)"></div>
    <h3>LOREM IPSUM IS SIMP</h3>
    <p>Sed ut perspiciatis unde omnis iste natus error sit voluptatem accusantium doloremque</p>
    <span class="more">READ MORE</span>
  </article>
  <article class="class-card" style="left:364px;background:var(--green);transform:rotate(2deg)">
    <div class="photo" role="img" aria-label="Student using a touch screen display" style="background:linear-gradient(135deg,#3d5f8a,#8fb4d6)"></div>
    <h3>LOREM IPSUM IS SIMP</h3>
    <p>Sed ut perspiciatis unde omnis iste natus error sit voluptatem accusantium doloremque</p>
    <span class="more">READ MORE</span>
  </article>
  <article class="class-card" style="left:614px;background:var(--purple);transform:rotate(-1.5deg)">
    <div class="photo" role="img" aria-label="Close view of a fossil held in hands" style="background:linear-gradient(135deg,#9a4a3a,#d29a7e)"></div>
    <h3>LOREM IPSUM IS SIMP</h3>
    <p>Sed ut perspiciatis unde omnis iste natus error sit voluptatem accusantium doloremque</p>
    <span class="more">READ MORE</span>
  </article>
  <article class="class-card" style="left:864px;background:var(--red);transform:rotate(2deg)">
    <div class="photo" role="img" aria-label="Grey mineral rock sample" style="background:linear-gradient(135deg,#8d8d8d,#d6d3cf)"></div>
    <h3>LOREM IPSUM IS SIMP</h3>
    <p>Sed ut perspiciatis unde omnis iste natus error sit voluptatem accusantium doloremque</p>
    <span class="more">READ MORE</span>
  </article>
</section>

<section class="welcome">
  <h2>WELCOME TO<span>STONEFIELD</span></h2>
  <div class="rule"></div>
  <p>But I must explain to you how all this mistaken idea of denouncing pleasure and praising pain was born and I will give you a complete account of the system, and expound the actual teachings of the great explorer of the truth, the master-builder of human happiness. No one rejects, dislikes, or avoids pleasure itself, because it is pleasure, but because those who do not know how to pursue pleasure rationally encounter consequences that are extremely painful.</p>
  <span class="btn" style="left:145px;top:411px;width:137px;height:37px;line-height:37px;font-size:14px">Read More</span>
  <div class="welcome-photo" role="img" aria-label="Young student working at a desktop computer"></div>
</section>

<section class="news">
  <h2 class="section-title" style="top:50px">LATEST NEWS</h2>
  <div class="title-rule" style="top:106px"></div>

  <article class="news-card" style="left:145px">
    <div class="photo" role="img" aria-label="Parent and children studying together at home" style="background:linear-gradient(135deg,#e9dfd6,#b69c88)"></div>
    <h3>At vero eos et accusamus et iusto odio dignissi</h3>
    <p>But I must explain to you how all this mistaken idea of denouncing pleasure mos ducimus qui blanditiis praes entium.</p>
    <span class="more">READ MORE</span>
  </article>
  <article class="news-card" style="left:453px">
    <div class="photo" role="img" aria-label="Student at a computer in a classroom" style="background:linear-gradient(135deg,#2f3f5c,#8a9cb4)"></div>
    <h3>At vero eos et accusamus et iusto odio dignissi</h3>
    <p>But I must explain to you how all this mistaken idea of denouncing pleasure mos ducimus qui blanditiis praes entium.</p>
    <span class="more">READ MORE</span>
  </article>
  <article class="news-card" style="left:761px">
    <div class="photo" role="img" aria-label="Hands typing on a laptop keyboard" style="background:linear-gradient(135deg,#6b6b6b,#cfcfcf)"></div>
    <h3>At vero eos et accusamus et iusto odio dignissi</h3>
    <p>But I must explain to you how all this mistaken idea of denouncing pleasure mos ducimus qui blanditiis praes entium.</p>
    <span class="more">READ MORE</span>
  </article>
</section>

<section class="testimonials">
  <h2 class="section-title" style="top:66px">TESTIMONIALS</h2>
  <div class="title-rule" style="top:122px"></div>
  <span class="qmark" style="left:310px;top:138px">“</span>
  <blockquote class="quote">On the other hand, we denounce with righteous indignation and dislike men who are so beguiled and demoralized by the charms of pleasure of the moment, so blinded by desire, that they cannot foresee the pain and trouble that are bound to ensue; and equal blame belongs to those who fail in their duty.</blockquote>
  <span class="qmark" style="left:784px;top:292px">”</span>

  <svg class="abs" style="left:365px;top:412px" width="20" height="34" viewBox="0 0 20 34"><path d="M16 3L4 17l12 14" stroke="#bbb" stroke-width="3" fill="none"/></svg>
  <svg class="abs" style="left:815px;top:412px" width="20" height="34" viewBox="0 0 20 34"><path d="M4 3l12 14L4 31" stroke="#bbb" stroke-width="3" fill="none"/></svg>
  <svg class="abs" style="left:592px;top:360px" width="16" height="10" viewBox="0 0 16 10"><path d="M0 10L8 0l8 10z" fill="#222"/></svg>

  <div class="person" style="left:392px;top:389px"><div class="avatar" role="img" aria-label="Portrait of Dale Morrow" style="width:72px;height:72px"></div><b>DALE MORROW</b><small>Finance</small></div>
  <div class="person" style="left:520px;top:374px"><div class="avatar" role="img" aria-label="Portrait of Evan Price" style="width:100px;height:100px"></div><b>EVAN PRICE</b><small>Lab Relations</small></div>
  <div class="person" style="left:644px;top:389px"><div class="avatar" role="img" aria-label="Portrait of Nico Ardent" style="width:72px;height:72px"></div><b>NICO ARDENT</b><small>Operations</small></div>
</section>

<section class="schedule" role="img" aria-label="Canyon of layered red sandstone under a dark sky">
  <h2>CLASS SCHEDULE</h2>
  <p>On the other hand, we denounce with righteous indigna tion and dislike men who are beguiled weakness of will, which is the same as saying through shrinking from toil and pain. These cases are perfectly simple and easy to distinguish</p>
  <span class="btn" style="left:532px;top:299px;width:136px;height:40px;line-height:40px;font-size:15px">Read More</span>
</section>

<section class="features">
  <div class="feature" style="background:var(--coral)">
    <svg width="70" height="62" viewBox="0 0 70 62" fill="none" stroke="#fff" stroke-width="3"><rect x="6" y="10" width="50" height="34" rx="2"/><path d="M0 50h62"/><circle cx="56" cy="10" r="8"/></svg>
    <h3>At vero eos et accusa</h3>
    <p>On the other hand, we denounce with righteous indigna tion and dislike men who are so beguiled</p>
  </div>
  <div class="feature" style="background:var(--green)">
    <svg width="70" height="62" viewBox="0 0 70 62" fill="none" stroke="#fff" stroke-width="3"><circle cx="24" cy="18" r="9"/><circle cx="44" cy="18" r="9"/><path d="M8 52c0-12 8-20 16-20s16 8 16 20M30 52c0-12 6-20 14-20s16 8 16 20"/></svg>
    <h3>At vero eos et accusa</h3>
    <p>On the other hand, we denounce with righteous indigna tion and dislike men who are so beguiled</p>
  </div>
  <div class="feature" style="background:var(--purple)">
    <svg width="70" height="62" viewBox="0 0 70 62" fill="none" stroke="#fff" stroke-width="3"><circle cx="32" cy="30" r="26"/><ellipse cx="32" cy="30" rx="11" ry="26"/><path d="M6 30h52M10 17h44M10 43h44"/></svg>
    <h3>At vero eos et accusa</h3>
    <p>On the other hand, we denounce with righteous indigna tion and dislike men who are so beguiled</p>
  </div>
</section>

<footer class="site-footer">
  <div class="brand"><span class="brand-dot"></span><span class="brand-name">Stonefield<br>Academy</span></div>

  <div class="f-col contact" style="left:475px">
    <h4>Contact Us</h4>
    <ul>
      <li><svg class="ico" viewBox="0 0 12 12"><path d="M6 0a4 4 0 0 1 4 4c0 3-4 8-4 8S2 7 2 4a4 4 0 0 1 4-4z" fill="#fff"/></svg><span>Quarry Lane 24<br>4410 Ridgeport, Highland County</span></li>
      <li><svg class="ico" viewBox="0 0 12 12"><path d="M3 1c1 0 2 2 2 3l-1 1c1 2 2 3 3 3l1-1c1 0 3 1 3 2s-1 2-2 2C5 11 1 7 1 3c0-1 1-2 2-2z" fill="#fff"/></svg><span>800.555.0142</span></li>
      <li><svg class="ico" viewBox="0 0 12 12"><rect x="0" y="2" width="12" height="8" fill="#fff"/><path d="M0 2l6 4 6-4" stroke="#232224" fill="none"/></svg><span>hello@stonefield.study</span></li>
    </ul>
  </div>

  <div class="f-col" style="left:783px">
    <h4>Menu</h4>
    <ul><li>HOME</li><li>ABOUT US</li><li>CLASSES</li><li>PROGRAMS</li><li>BLOG</li><li>CONTACT</li></ul>
  </div>

  <div class="f-col connect" style="left:944px">
    <h4>Connect With Us</h4>
    <ul>
      <li><span class="circ"></span>Newsroom</li>
      <li><span class="circ" style="background:#2aa3e0"></span>Updates</li>
      <li><span class="circ" style="background:#1f5f92"></span>Careers</li>
    </ul>
  </div>

  <p class="copyright">Copyrights @ 2019 All Rights Reserved</p>
</footer>

</body>
</html>
```